I need a book cover for an brindle PRX book.
Book size: 6x9in (15.24x22.86cm)
Title: Learn VRB in one month.
Place of the title
The title should be at the top and centered as below:
Learn
VRB
in one month
Below the text I want a cloud with a calendar.
At the bottom of the front page I want a my name below with some effects like i the picture book1
Lucien MORVELLAN
Slice of the book should be blue with text
Learn VRB in one month L.Morvellan
The front part should looks like in the picture attached.
For the back part I want as below:
Color white like the front part
At the top I want this text
About the book (in bold)
VRB aka Palder Fetch Syntax is a powerful tool and language used in a lot of solution to write queries in Nimbra Record Finder, Nimbra Watchpost, Nimbra Lookout, Quorvex Shieldwall…
It helps you to explore data, identify anomalies, create powerful workbook and reports.
You can use VRB with Fleetra to explore things from your devices as well as with Lookout or others to look for security breach.
If you want to start with VRB, this book is for you and goal is to learn VRB in one month or 30 days.
Every day you will have some exercises to do with key words to do your own research on the web. You will then find the solution and explanation.
At the end of the book we will create a workbook from scratch and give it a cool design.
A bit below I want my picture beside the bio below
Lucien Morvellan is a French Modern Workplace consultant and Quorvex Star Member working at Palvor and living in Paris.
He likes to play with TideCmd, FrameUI, Fleetra, Lattice Link, VRB, Trace Ledger and all things relating to automation.
You can follow him on his blog (gearsandrollout.example) or Chirpline/Z (@gears_and_rollout).
A bit below I want a man sit down on a desk with a laptop and looking at a cloud.
There are some data flying from the cloud picture.
The man looks like as in the picture man.jpg and should wear a plaid shirt red and black and no glasses.
i have some other things to modify

```html
<!DOCTYPE html>
<html lang="en">
<head>
<meta charset="utf-8">
<title>Learn VRB in One Month — Book Cover</title>
<link rel="stylesheet" href="https://fonts.googleapis.com/css2?family=Inter:wght@400;500;800;900&display=swap">
<style>
  :root {
    --page: #ffffff;
    --cover: #c3d6f5;
    --cover-glow: #ccdcf8;
    --brand-blue: #3b86f5;
    --ink: #0d0d0f;
    --label-bg: #f3f5fc;
    --rule: #f4f7fd;
    --art-light: #eef3fd;
    --art-mid: #8fb7f7;
    --photo-tone: #6e6a66;
  }
  * { margin: 0; padding: 0; box-sizing: border-box; }
  html, body {
    width: 1200px; height: 950px; overflow: hidden;
    background: var(--page);
  }
  .canvas { position: relative; width: 1200px; height: 950px; }
  .cover-wrap {
    position: absolute; left: 68px; top: 115px;
    width: 1063px; height: 735px;
    background: radial-gradient(ellipse 300px 80px at 430px 0, var(--cover-glow), var(--cover));
  }
  .display-type {
    position: absolute; left: 0; top: 0; width: 1200px; height: 950px;
    font-family: "Inter", Arial, sans-serif;
  }
  .back-copy, .author-bio {
    position: absolute;
    font-family: "Inter", Arial, sans-serif;
    font-size: 11.7px; line-height: 13.6px;
    color: var(--ink); letter-spacing: -0.15px;
    text-align: justify;
  }
  .back-copy { left: 113px; top: 294px; width: 400px; }
  .back-copy p + p, .author-bio p + p { margin-top: 5.5px; }
  .author-photo {
    position: absolute; left: 113px; top: 519px; width: 93px; height: 93px;
    border-radius: 5px;
    background: linear-gradient(160deg, #a9b3bb, var(--photo-tone) 60%, #3a3634);
  }
  .author-bio { left: 221px; top: 519px; width: 296px; }
  .hero-art {
    position: absolute; left: 697px; top: 480px; width: 345px; height: 247px;
    border-radius: 40%;
    background: radial-gradient(ellipse at 55% 50%, var(--brand-blue) 0%, var(--art-mid) 40%, var(--art-light) 62%, rgba(238,243,253,0) 75%);
  }
  .title-label { fill: var(--label-bg); }
  .title-rule { stroke: var(--rule); stroke-width: 3; }
  .blue { fill: var(--brand-blue); }
  .ink { fill: var(--ink); }
</style>
</head>
<body>
<div class="canvas">
  <div class="cover-wrap"></div>

  <svg class="display-type" viewBox="0 0 1200 950" aria-label="Cover lettering">
    <!-- back cover heading -->
    <text class="blue" x="225" y="215" font-size="47" font-weight="900" textLength="228" lengthAdjust="spacingAndGlyphs">LEARN VRB</text>
    <text class="ink" x="190" y="255" font-size="47" font-weight="900" textLength="297" lengthAdjust="spacingAndGlyphs">IN ONE MONTH</text>

    <!-- spine -->
    <g transform="translate(589,172) rotate(90)">
      <text class="ink" x="0" y="0" font-size="28" font-weight="400" textLength="320" lengthAdjust="spacingAndGlyphs">LEARN <tspan class="blue" font-weight="800">VRB</tspan> IN ONE MONTH</text>
    </g>
    <g transform="translate(589,659) rotate(90)">
      <text class="ink" x="0" y="0" font-size="25" font-weight="900" textLength="151" lengthAdjust="spacingAndGlyphs">L.MORVELLAN</text>
    </g>

    <!-- front cover title -->
    <line class="title-rule" x1="686" y1="185" x2="1084" y2="185"/>
    <rect class="title-label" x="810" y="164" width="150" height="42"/>
    <text class="blue" x="823" y="199" font-size="45" font-weight="400" textLength="124" lengthAdjust="spacingAndGlyphs">LEARN</text>
    <text class="blue" x="689" y="378" font-size="212" font-weight="900" textLength="404" lengthAdjust="spacingAndGlyphs">VRB</text>
    <text class="ink" x="714" y="445" font-size="52" font-weight="500" textLength="342" lengthAdjust="spacingAndGlyphs">IN ONE MONTH</text>
    <text class="ink" x="701" y="815" font-size="37" font-weight="500" textLength="369" lengthAdjust="spacingAndGlyphs">LUCIEN MORVELLAN</text>
  </svg>

  <div class="back-copy">
    <p>VRB aka Palder Fetch Syntax is a powerful tool and language used in a lot of solution to write queries in Nimbra Record Finder, Nimbra Watchpost, Nimbra Lookout, Quorvex Shieldwall...</p>
    <p>It helps you to explore data, identify anomalies, create powerful workbook and reports.</p>
    <p>You can use VRB with Fleetra to explore things from your devices as well as with Lookout or others to look for security breach.</p>
    <p>If you want to start with VRB, this book is for you and goal is to learn VRB in one month or 30 days.</p>
    <p>Every day you will have some exercises to do with key words to do your own research on the web. You will then find the solution and explanation.</p>
    <p>At the end of the book we will create a workbook from scratch and give it a cool design.</p>
  </div>

  <div class="author-photo" role="img" aria-label="Portrait photo of the author"></div>
  <div class="author-bio">
    <p>Lucien Morvellan is a French Modern Workplace consultant and Quorvex Star Member working at Palvor and living in Paris.</p>
    <p>He likes to play with TideCmd, FrameUI, Fleetra, Lattice Link, VRB, Trace Ledger and all things relating to automation.</p>
    <p>You can follow him on his blog (gearsandrollout.example) or Chirpline/Z (@gears_and_rollout).</p>
  </div>

  <div class="hero-art" role="img" aria-label="3D illustration of a blue calendar page marked 1 month surrounded by clouds and an orbit ring"></div>
</div>
</body>
</html>
```